Simple, Professional and neat business card design for Vendralo Inc.

We're looking to re-vamp our business card design. We're a supplier of innovative feed ingredients for the North American animal agriculture industry. We are located in Lucknow, Ontario, Canada and our flagship product is a product that prevents milk fever in dairy cows when the calve, it is fed before calving and is very effective compared to other alternatives available on the market today.

Our company has Danish roots and we import all of our product from our Danish partner/manufacturer in Denmark. We like our design to embrace high professionalism while remaining neat and simple.

Target Market(s)

B2B, Feed Mills, Veterinary Clinics, Large integrators/producers,

Industry/Entity Type

Agribusiness

Contact Information for Business Card

We like the rounded corners because they make the card easy to sit in a wallet and not many use it so it makes the card stand out, just possibly something to take account for during the design.

As you can also see on the sliders below, looking for a that simple but proffesional scandinavian design.

Requirements
Nice to have
• Rounded corners
Should not have
• Too vibrant

```html
<!DOCTYPE html>
<html lang="en">
<head>
<meta charset="utf-8">
<title>Vendralo Inc. — Business Card</title>
<link href="https://fonts.googleapis.com/css2?family=Lato:wght@400;700&display=swap" rel="stylesheet">
<style>
  :root {
    --backdrop: #2b2d31;
    --card-dark: #1f1f20;
    --card-light: #ffffff;
    --brand-blue: #1565c0;
    --text-light: #f2f2f2;
    --text-muted: #d6d6d6;
  }
  * { box-sizing: border-box; margin: 0; padding: 0; }
  html, body {
    width: 1200px; height: 900px; overflow: hidden;
    background: var(--backdrop);
    font-family: 'Lato', sans-serif;
  }
  .sheet {
    width: 1200px; height: 900px;
    display: flex; flex-direction: column; align-items: center; justify-content: center;
    gap: 60px;
  }
  .card {
    width: 612px; height: 350px;
    border-radius: 30px;
    position: relative;
    box-shadow: 0 14px 30px rgba(0,0,0,.35);
  }
  .card--front { background: var(--card-dark); }
  .card--back { background: var(--card-light); display: flex; align-items: center; justify-content: center; }

  .brand { display: flex; align-items: center; gap: 10px; color: var(--brand-blue); font-weight: 700; text-transform: uppercase; letter-spacing: .5px; }
  .brand__dot { width: 22px; height: 22px; border-radius: 50%; background: var(--brand-blue); flex: none; }
  .card--front .brand { position: absolute; left: 48px; top: 56px; font-size: 24px; }
  .card--back .brand { font-size: 40px; gap: 16px; }
  .card--back .brand__dot { width: 38px; height: 38px; }

  .divider { position: absolute; left: 250px; top: 140px; width: 2px; height: 170px; background: var(--brand-blue); }

  .details { position: absolute; left: 278px; top: 136px; color: var(--text-light); }
  .details__name { font-size: 34px; font-weight: 400; color: var(--brand-blue); line-height: 1.1; }
  .details__role { font-size: 20px; font-weight: 700; margin-top: 4px; }
  .details__address { font-size: 15px; color: var(--text-muted); line-height: 1.35; margin-top: 6px; }
  .contact { list-style: none; margin-top: 8px; font-size: 15px; line-height: 1.5; }
  .contact li { display: flex; align-items: center; gap: 8px; }
  .contact svg { width: 15px; height: 15px; flex: none; }
  .contact__web { color: var(--brand-blue); }
</style>
</head>
<body>
<main class="sheet">
  <section class="card card--front" aria-label="Card front">
    <div class="brand"><span class="brand__dot"></span>Vendralo Inc.</div>
    <div class="divider"></div>
    <div class="details">
      <h1 class="details__name">Elin Marsh</h1>
      <p class="details__role">Director</p>
      <p class="details__address">118 Meadow Road<br>Fairhill, ON N0G 1K0</p>
      <ul class="contact">
        <li>
          <svg viewBox="0 0 24 24" fill="#1565c0"><path d="M6.6 10.8a15.1 15.1 0 0 0 6.6 6.6l2.2-2.2c.3-.3.7-.4 1-.2 1.1.4 2.3.6 3.6.6.6 0 1 .4 1 1V20c0 .6-.4 1-1 1A17 17 0 0 1 3 4c0-.6.4-1 1-1h3.5c.6 0 1 .4 1 1 0 1.3.2 2.5.6 3.6.1.3 0 .7-.2 1z"/></svg>
          +1 555 014 2276
        </li>
        <li>
          <svg viewBox="0 0 24 24" fill="none" stroke="#1565c0" stroke-width="2"><rect x="3" y="5" width="18" height="14" rx="1"/><path d="M3 6l9 7 9-7"/></svg>
          elin@vendralofeeds.com
        </li>
        <li class="contact__web">
          <svg viewBox="0 0 24 24" fill="none" stroke="#1565c0" stroke-width="2"><circle cx="12" cy="12" r="9"/><path d="M3 12h18M12 3c3 3 3 15 0 18M12 3c-3 3-3 15 0 18"/></svg>
          vendralofeeds.com
        </li>
      </ul>
    </div>
  </section>

  <section class="card card--back" aria-label="Card back">
    <div class="brand"><span class="brand__dot"></span>Vendralo Inc.</div>
  </section>
</main>
</body>
</html>
```